Copper Lantern Coffee Bean Labels

We need a label for a new brand of coffee that we are selling in Portland, Oregon (Coffee Capital). Our company has no current online presence but have some great roasting techniques. We will be roasting our own coffee beans from throughout the world and selling them immediately after roasting causing a super fresh and high quality product.

We will be packaging in brown kraft bags: 3 3/8 X 2.5 x 7.75 inches which is standard for coffee beans.

Also notice on that sample the blue section in the middle has the product name. We want to also make it so that there is a consistent area that we can print OVER the label the name or blend of the coffee.

Our company is called Copper Lantern Coffee Roasters. We will want to put copperlanternroasters.example on the label someplace (we dont have a site yet but will by launch).

We need to incorporate A Black Diamond into the design. No preferences yet on the style of it.

We want to be a super-premium brand. Sort of like MicroBrew beers. We will sell at Farmers Markets, online, and directly into stores. Image is very important to us.

Labels should be about 3" wide and about 3.75" high.. Perhaps higher if a cool design justifies the height. Again we will be using a brown kraft bag (like grocery bag color) as shown on the sample.

SEE ATTACHED SEVERAL INTERESTING DESIGNS

Target Market(s)

Foodies, Yuppie, Coffee Snob

Industry/Entity Type

It Company

Requirements
Must have
• Location for the product Name to go onto it... We want to use the same labels for our full line. Just printing over it something like "Italian Roast" and a line below saying something like "Bold, Nutty Flavor, blah blah"

Should not have
• Clunkey looking old fonts or things that look homemade.

```html
<!DOCTYPE html>
<html lang="en">
<head>
<meta charset="utf-8">
<title>Copper Lantern Coffee Roasters – Bean Label</title>
<link rel="stylesheet" href="https://fonts.googleapis.com/css2?family=Cinzel:wght@400;700&family=Berkshire+Swash&family=Montserrat:wght@800&display=swap">
<style>
  :root {
    --paper: #ffffff;
    --frame: #141010;
    --kraft: #c69c6c;
    --kraft-deep: #b88c5c;
    --cocoa: #8c7264;
    --cocoa-dark: #6b5446;
    --seal: #7e6a62;
    --ink: #221612;
    --band: #ffffff;
  }
  * { margin: 0; padding: 0; box-sizing: border-box; }
  html, body {
    width: 840px;
    height: 1200px;
    overflow: hidden;
    background: var(--paper);
  }
  .label {
    position: absolute;
    left: 60px;
    top: 40px;
    width: 720px;
    height: 1120px;
    border: 6px solid var(--frame);
    overflow: hidden;
  }
  .label-art {
    position: absolute;
    inset: 0;
    width: 100%;
    height: 100%;
  }
  .brand-name {
    position: absolute;
    left: 0;
    width: 100%;
    text-align: center;
    font-family: "Cinzel", serif;
    font-weight: 700;
    color: var(--ink);
    letter-spacing: 2px;
  }
  .brand-name--top { top: 150px; font-size: 64px; }
  .brand-name--bottom { top: 505px; font-size: 40px; letter-spacing: 3px; }
  .origin-line {
    position: absolute;
    top: 598px;
    left: 0;
    width: 100%;
    text-align: center;
    font-family: "Cinzel", serif;
    font-size: 24px;
    color: var(--ink);
    letter-spacing: 1px;
  }
  .product-title {
    position: absolute;
    top: 700px;
    left: 0;
    width: 100%;
    text-align: center;
    font-family: "Cinzel", serif;
    font-weight: 400;
    font-size: 62px;
    line-height: 80px;
    color: var(--ink);
    letter-spacing: 4px;
  }
  .tagline {
    position: absolute;
    top: 955px;
    left: 0;
    width: 100%;
    text-align: center;
    font-family: "Berkshire Swash", cursive;
    font-size: 46px;
    color: var(--ink);
  }
  .tagline .star { font-size: 30px; margin: 0 14px; vertical-align: middle; }
  .divider {
    position: absolute;
    top: 1030px;
    left: 250px;
    width: 208px;
    height: 6px;
    border-radius: 3px;
    background: var(--ink);
  }
  .web-address {
    position: absolute;
    top: 1070px;
    left: 0;
    width: 100%;
    text-align: center;
    font-family: "Montserrat", sans-serif;
    font-weight: 800;
    font-size: 21px;
    color: var(--frame);
    letter-spacing: 1px;
  }
</style>
</head>
<body>
  <main class="label">
    <svg class="label-art" viewBox="0 0 708 1108" preserveAspectRatio="none" aria-hidden="true">
      <rect class="kraft-field" x="0" y="0" width="708" height="880" fill="var(--kraft)"/>
      <path class="cocoa-field" d="M0 860 H708 V1108 H0 Z" fill="var(--cocoa)"/>
      <path class="top-band" d="M0 0 H708 V44 Q354 20 0 44 Z" fill="var(--cocoa-dark)"/>
      <path class="title-band" d="M0 650 Q354 608 708 650 V880 Q354 840 0 880 Z" fill="var(--band)"/>
      <circle class="seal" cx="354" cy="385" r="118" fill="var(--seal)"/>
    </svg>
    <div class="kraft-pattern" role="img" aria-label="Subtle interlocking circle pattern across the kraft panels" hidden></div>

    <p class="brand-name brand-name--top">Copper Lantern</p>
    <p class="brand-name brand-name--bottom">COFFEE ROASTERS</p>
    <p class="origin-line">PORTLAND, OR • EST. 2013</p>

    <h1 class="product-title">100 PERCENT<br>COFFEE TITLE</h1>

    <p class="tagline">Super Fresh<span class="star">✲</span>High Quality</p>
    <div class="divider" role="img" aria-label="Ornamental divider"></div>
    <p class="web-address">www.COPPERLANTERNROASTERS.example</p>
  </main>
</body>
</html>
```